computter lessons

new business venture [ self employed ] will register my business name as " KEYVORLAN "
what I will offer is :-
computer lessons for new beginners.
Initial set up and basic overview.
lessons per hour in the comfort of your own home.
special rates for customers aged 50+
First lesson is half price with no obligation for booking any further appointments.
a learning and training plan will be presented based on your requirements.
an appraisal update on your new skills.

contact info:-
0161 4970213
07700 900482
larkden@mervoxmail.com

```html
<!DOCTYPE html>
<html lang="en">
<head>
<meta charset="utf-8">
<title>KEYVORLAN – Computer Classes for Beginners</title>
<link rel="stylesheet" href="https://fonts.googleapis.com/css2?family=Anton&family=Fira+Sans:wght@600;700&family=Oswald:wght@500;700&family=Roboto+Condensed:wght@400;500&display=swap">
<style>
  :root {
    --teal: #1b8587;
    --teal-ink: #177a7b;
    --paper: #f7f7f5;
    --backdrop: #e3e9e9;
    --white: #ffffff;
    --photo-light: #e9eaea;
    --photo-dark: #9aa0a3;
  }
  * { box-sizing: border-box; margin: 0; padding: 0; }
  html, body { width: 1135px; height: 1200px; overflow: hidden; background: var(--backdrop); }
  .flyer {
    position: absolute; left: 167px; top: 33px;
    width: 800px; height: 1133px;
    background: var(--paper);
    color: var(--teal-ink);
    overflow: hidden;
  }
  .flyer__header {
    position: absolute; left: 0; top: 0; width: 100%; height: 108px;
    background: var(--teal);
    display: flex; align-items: center; justify-content: center;
  }
  .flyer__title {
    font-family: "Fira Sans", sans-serif; font-weight: 700;
    font-size: 45px; color: var(--white); letter-spacing: 0.3px;
  }
  .hero-photo {
    position: absolute; left: 205px; top: 255px; width: 416px; height: 320px;
    z-index: 1;
    background: radial-gradient(ellipse at 55% 45%, var(--photo-dark) 0%, #c4c8ca 45%, var(--photo-light) 75%, var(--paper) 100%);
  }
  .bubble {
    position: absolute; border-radius: 50%; z-index: 2;
    background: var(--teal); color: var(--white);
    display: flex; align-items: center; justify-content: center;
    text-align: center; font-family: "Fira Sans", sans-serif; font-weight: 600;
    line-height: 1.2;
  }
  .bubble--wish { left: 116px; top: 160px; width: 183px; height: 112px; font-size: 18px; }
  .bubble--start { left: 522px; top: 180px; width: 130px; height: 76px; font-size: 15px; }
  .bubble--dot { font-size: 0; }
  .question-mark {
    position: absolute; left: 368px; top: 146px; z-index: 2;
    font-family: "Fira Sans", sans-serif; font-weight: 700;
    font-size: 100px; line-height: 1; color: var(--teal);
  }
  .offer-list {
    position: absolute; left: 54px; top: 625px; width: 449px; height: 248px;
    border: 4px solid var(--teal); border-radius: 10px;
    list-style: none; padding: 20px 12px 0 12px;
    display: flex; flex-direction: column; gap: 21px;
    font-family: "Roboto Condensed", sans-serif; font-weight: 500;
    font-size: 17px; line-height: 21px;
  }
  .offer-list__item { display: flex; gap: 12px; align-items: flex-start; }
  .offer-list__tick { flex: 0 0 22px; height: 21px; }
  .offer-list__item--small { font-size: 15.5px; }
  .promo { position: absolute; left: 528px; width: 246px; text-align: center; }
  .promo--rates { top: 636px; }
  .promo--half { top: 760px; }
  .promo__headline {
    display: inline-block;
    font-family: "Anton", sans-serif; font-weight: 400;
    font-size: 52px; line-height: 1.05; white-space: nowrap;
    transform: scaleX(0.8); transform-origin: center;
    margin: 0 -40px;
  }
  .promo__note {
    font-family: "Roboto Condensed", sans-serif; font-weight: 500;
    font-size: 22px; line-height: 1.25; white-space: nowrap;
  }
  .brand {
    position: absolute; left: 0; width: 800px; top: 900px;
    display: flex; align-items: center; justify-content: center; gap: 14px;
  }
  .brand__mark { width: 44px; height: 44px; border-radius: 50%; background: var(--teal); }
  .brand__name {
    font-family: "Oswald", sans-serif; font-weight: 700;
    font-size: 60px; line-height: 1; color: var(--teal-ink);
  }
  .email {
    position: absolute; left: 0; width: 800px; top: 968px; text-align: center;
    font-family: "Roboto Condensed", sans-serif; font-weight: 400; font-size: 34px;
  }
  .flyer__footer {
    position: absolute; left: 0; bottom: 0; width: 100%; height: 84px;
    background: var(--teal);
    display: flex; align-items: center; justify-content: center;
    font-family: "Oswald", sans-serif; font-weight: 500;
    font-size: 46px; color: var(--white); white-space: nowrap; letter-spacing: -0.5px;
  }
  .flyer__footer-label { margin-right: 22px; }
</style>
</head>
<body>
  <main class="flyer">
    <header class="flyer__header">
      <h1 class="flyer__title">Computer Classes for Beginners</h1>
    </header>

    <div class="hero-photo" role="img" aria-label="Photo of a puzzled older man in shirt and tie resting his chin on his hand in front of a laptop, with a phone on the desk"></div>

    <div class="bubble bubble--wish">Wish I had<br>learned computer...</div>
    <div class="bubble bubble--dot" style="left:275px;top:262px;width:30px;height:24px"></div>
    <div class="bubble bubble--dot" style="left:313px;top:286px;width:22px;height:16px"></div>
    <div class="bubble bubble--dot" style="left:335px;top:301px;width:16px;height:13px"></div>

    <div class="question-mark">?</div>

    <div class="bubble bubble--start">But where<br>Do I START?</div>
    <div class="bubble bubble--dot" style="left:530px;top:249px;width:24px;height:19px"></div>
    <div class="bubble bubble--dot" style="left:510px;top:267px;width:18px;height:14px"></div>
    <div class="bubble bubble--dot" style="left:491px;top:280px;width:16px;height:13px"></div>

    <ul class="offer-list">
      <li class="offer-list__item"><svg class="offer-list__tick" viewBox="0 0 22 21"><path d="M2 11 L8 17 L20 4" fill="none" stroke="#1b8587" stroke-width="4" stroke-linecap="round" stroke-linejoin="round"/></svg><span>Computer lessons for new beginners</span></li>
      <li class="offer-list__item"><svg class="offer-list__tick" viewBox="0 0 22 21"><path d="M2 11 L8 17 L20 4" fill="none" stroke="#1b8587" stroke-width="4" stroke-linecap="round" stroke-linejoin="round"/></svg><span>Initial set up and basic overview</span></li>
      <li class="offer-list__item"><svg class="offer-list__tick" viewBox="0 0 22 21"><path d="M2 11 L8 17 L20 4" fill="none" stroke="#1b8587" stroke-width="4" stroke-linecap="round" stroke-linejoin="round"/></svg><span>Lessons per hour in the comfort of your own home</span></li>
      <li class="offer-list__item"><svg class="offer-list__tick" viewBox="0 0 22 21"><path d="M2 11 L8 17 L20 4" fill="none" stroke="#1b8587" stroke-width="4" stroke-linecap="round" stroke-linejoin="round"/></svg><span>A learning and training plan presented based on your requirements</span></li>
      <li class="offer-list__item offer-list__item--small"><svg class="offer-list__tick" viewBox="0 0 22 21"><path d="M2 11 L8 17 L20 4" fill="none" stroke="#1b8587" stroke-width="4" stroke-linecap="round" stroke-linejoin="round"/></svg><span>An appraisal update on your new skills</span></li>
    </ul>

    <div class="promo promo--rates">
      <div class="promo__headline">SPECIAL RATES</div>
      <div class="promo__note">For Customers aged 50+</div>
    </div>
    <div class="promo promo--half">
      <div class="promo__headline">HALF PRICE</div>
      <div class="promo__note">First Lesson. No Obligation</div>
    </div>

    <div class="brand">
      <span class="brand__mark"></span>
      <span class="brand__name">KEYVORLAN</span>
    </div>
    <div class="email">larkden@mervoxmail.com</div>

    <footer class="flyer__footer">
      <span class="flyer__footer-label">CALL NOW</span>
      <span>0161 4970213 / 07700 900482</span>
    </footer>
  </main>
</body>
</html>
```